今回はコーポレートサイトのTOPページのデザインをお願いしたく思います。

【素材】
素材に関しては、ロゴや写真等は現在準備中でして、
デザインの際は仮のオブジェクトを入れて対応して頂ければと思います。

【サイト構成】
サイトの構成については、ラフを書きましたので下記URLからダウンロードお願いします。
http://qvn.jp/PbLwoR

※PCを想定したデザインでお願いいたします。

【イメージ】
以下が現在の「アオバエステート株式会社」のコーポレートサイトになります。
http://www.aoba-estate.co.jp/

今回ご提案いただく新しいサイトのデザインは上記のものから一新して

1.スタイリッシュ
2.NY
3.最先端
4.近未来
5.エネルギッシュ
6.エキサイティング
7.自由
8.それでいてシンプル

なイメージ、従来の不動産会社のイメージに囚われないものにしたく思います。

【参考サイト】
https://www.kumonomi.co.jp/

1ページ
グレー系
今回のデザインで採用させて頂いた方には、
コーポレートサイトの「代表メッセージ」「ニュース」「投資実績」の他3ページのデザインやコーディングなど、他のお仕事に関してもご相談させて頂ければと思います。
(もちろん当案件のみご希望の方からも募集しており、採用有無には関係ありません。)

色のコンセプトと対応の早さ、デザインの良さで決定致しました。

皆さま、お忙しい所多くのご提案を頂きまして誠にありがとうございます。
また何かございましたらお願いをさせて頂きますので引き続き宜しくお願い致します。

```html
<!DOCTYPE html>
<html lang="ja">
<head>
<meta charset="utf-8">
<title>AOBA ESTATE | アオバエステート株式会社</title>
<link rel="stylesheet" href="https://fonts.googleapis.com/css2?family=Montserrat:wght@400;500;600&family=Noto+Sans+JP:wght@400;500;700&family=Playfair+Display:ital@1&display=swap">
<style>
:root{
  --red:#c4161c;
  --red-deep:#8e0d12;
  --ink:#222;
  --dark:#2a2a2a;
  --mid:#555;
  --grey:#f0f0f0;
  --line:#d6d6d6;
  --white:#fff;
}
*{box-sizing:border-box;margin:0;padding:0}
html,body{width:1200px;height:3208px;overflow:hidden}
body{font-family:"Noto Sans JP",sans-serif;color:var(--ink);background:var(--white);position:relative}
.en{font-family:"Montserrat",sans-serif}
section,header,footer{position:absolute;left:0;width:1200px}

/* header */
.site-header{top:0;height:80px;z-index:5;color:var(--white)}
.site-header .brand{position:absolute;left:40px;top:22px;font:500 26px/1 "Montserrat",sans-serif;letter-spacing:.12em}
.global-nav{position:absolute;right:190px;top:22px;display:flex;gap:34px;font:500 13px/1 "Montserrat",sans-serif;letter-spacing:.1em}
.global-nav .is-current{border-bottom:1px solid var(--white);padding-bottom:4px}
.sub-nav{position:absolute;left:540px;top:56px;display:flex;font-size:11px;background:rgba(255,255,255,.9);color:var(--ink)}
.sub-nav span{padding:6px 22px;border-right:1px solid var(--line)}
.header-contact{position:absolute;right:0;top:0;width:160px;height:80px;background:var(--red);text-align:center;padding-top:20px;font:500 13px/1 "Montserrat",sans-serif;letter-spacing:.12em}
.header-contact svg{display:block;margin:10px auto 0}

/* hero */
.hero{top:0;height:600px;background:linear-gradient(180deg,#1c1c1c 0%,#4a4a4a 45%,#2c2c2c 100%);color:var(--white);text-align:center}
.hero-title{position:absolute;top:248px;width:100%;font:500 64px/1 "Montserrat",sans-serif;letter-spacing:.32em;padding-left:.32em}
.hero-tagline{position:absolute;top:330px;width:100%;font:italic 30px/1 "Playfair Display",serif;color:var(--red);letter-spacing:.04em}
.hero-dots{position:absolute;top:562px;left:0;width:100%;display:flex;justify-content:center;gap:10px}
.hero-dots i{width:12px;height:12px;background:rgba(255,255,255,.5)}
.hero-dots i.on{background:var(--red)}

/* philosophy */
.philosophy{top:600px;height:372px;background:var(--dark)}
.philosophy-panel{position:absolute;left:0;top:0;width:600px;height:372px;background:linear-gradient(90deg,var(--red-deep),var(--red))}
.philosophy-photo{position:absolute;left:600px;top:0;width:600px;height:372px;background:linear-gradient(90deg,#6b6b6b,#cfcfcf)}
.philosophy-head{position:absolute;left:600px;top:70px;transform:translateX(-50%);text-align:center;color:var(--white)}
.philosophy-head h2{font:500 28px/1 "Montserrat",sans-serif;letter-spacing:.3em}
.philosophy-head p{font-size:14px;margin-top:12px;letter-spacing:.2em}
.philosophy-statement{position:absolute;left:0;top:232px;width:1200px;text-align:center;color:var(--white);font-size:22px;font-weight:700;letter-spacing:.08em}

/* section headings */
.section-head{text-align:center}
.section-head h2{font:500 26px/1 "Montserrat",sans-serif;letter-spacing:.3em;padding-left:.3em}
.section-head p{font-size:13px;margin-top:10px;letter-spacing:.2em}
.section-head .rule{width:60px;height:2px;background:var(--red);margin:10px auto 0}

/* works */
.works{top:972px;height:628px;background:var(--grey)}
.works .section-head{position:absolute;top:88px;width:100%}
.works-track{position:absolute;top:188px;left:0;width:1200px;height:300px}
.work-card{position:absolute;top:0;height:300px;overflow:hidden}
.work-photo{width:100%;height:240px}
.work-caption{height:60px;background:var(--white);padding:20px 18px;font-size:14px;font-weight:500}
.work-tag{position:absolute;top:0;left:0;background:var(--red);color:var(--white);font-size:12px;padding:7px 14px}
.work-card.left{left:-360px;width:600px}
.work-card.left .work-caption{padding-left:370px}
.work-card.center{left:248px;width:600px}
.work-card.right{left:856px;width:600px}
.slider-arrow{position:absolute;top:310px;width:44px;height:44px;display:flex;align-items:center;justify-content:center}
.btn-outline{position:absolute;display:flex;align-items:center;justify-content:center;gap:10px;border:1px solid var(--ink);background:var(--white);font-size:13px}
.works .btn-outline{top:528px;left:480px;width:240px;height:48px}

/* news */
.news{top:1600px;height:532px;background:var(--white)}
.news .section-head{position:absolute;top:80px;left:0;width:748px}
.news-list{position:absolute;top:156px;left:140px;width:560px;list-style:none}
.news-list li{display:flex;gap:26px;padding:16px 0;border-bottom:1px solid var(--line);font-size:12px;line-height:1.7}
.news-list time{font-family:"Montserrat",sans-serif;font-size:12px;color:var(--mid);white-space:nowrap;padding-top:1px}
.news .btn-outline{top:460px;left:314px;width:200px;height:40px}
.news-links{position:absolute;left:748px;top:12px;width:452px}
.news-link{position:relative;height:156px;margin-bottom:14px;color:var(--white);display:flex;align-items:center}
.news-link .photo{position:absolute;right:0;top:0;width:220px;height:100%}
.news-link .label{position:relative;padding-left:50px}
.news-link .label strong{display:block;font-size:18px;letter-spacing:.06em}
.news-link .label span{display:block;font-size:12px;margin-top:10px;opacity:.85}
.news-link.dark{background:#3a3a3a}
.news-link.red{background:var(--red)}

/* company */
.company{top:2140px;height:340px;background:linear-gradient(180deg,#3a3a3a,#1f1f1f);color:var(--white)}
.company .section-head{position:absolute;top:48px;width:100%}
.company-menu{position:absolute;top:148px;left:260px;width:680px;display:grid;grid-template-columns:320px 320px;gap:24px 40px}
.company-menu span{height:56px;background:rgba(0,0,0,.6);display:flex;align-items:center;justify-content:center;font-size:15px;letter-spacing:.1em}

/* map */
.access-map{top:2480px;height:420px;background:linear-gradient(135deg,#e6e6e6,#cfcfcf)}
.map-pin{position:absolute;left:580px;top:50px}

/* footer */
.site-footer{top:2900px;height:308px;background:var(--dark);color:var(--white)}
.footer-nav{position:absolute;left:40px;top:58px;display:flex;gap:34px;font:500 11px/1 "Montserrat",sans-serif;letter-spacing:.1em;color:#ccc}
.footer-contact{position:absolute;left:600px;top:10px;width:400px;height:70px;background:var(--red);display:flex;align-items:center;justify-content:center;gap:18px;font:500 18px/1 "Montserrat",sans-serif;letter-spacing:.2em}
.footer-tel{position:absolute;left:600px;top:108px;font:600 26px/1 "Montserrat",sans-serif;letter-spacing:.06em}
.footer-hours{position:absolute;left:900px;top:116px;font-size:11px;color:#bbb}
.footer-brand{position:absolute;left:40px;top:186px}
.footer-brand .name{font:500 24px/1 "Montserrat",sans-serif;letter-spacing:.16em}
.footer-brand .ja{font-size:12px;margin-top:10px}
.footer-brand .addr{font-size:10px;color:#bbb;margin-top:8px}
.copyright{position:absolute;left:40px;top:276px;font:400 10px/1 "Montserrat",sans-serif;color:#999}
</style>
</head>
<body>

<section class="hero" role="img" aria-label="白い外壁の住宅を見上げたモノクロの写真">
  <h1 class="hero-title">AOBA ESTATE</h1>
  <p class="hero-tagline">New way of real estate</p>
  <div class="hero-dots"><i class="on"></i><i></i><i></i></div>
</section>

<header class="site-header">
  <div class="brand">AOBA ESTATE</div>
  <nav class="global-nav">
    <span>HOME</span><span class="is-current">COMPANY</span><span>WORKS</span><span>NEWS</span><span>RECRUIT</span>
  </nav>
  <div class="sub-nav"><span>ご挨拶</span><span>会社概要</span><span>会社沿革</span></div>
  <div class="header-contact">CONTACT
    <svg width="20" height="14" viewBox="0 0 20 14" fill="none" stroke="#fff" stroke-width="1.5"><rect x="1" y="1" width="18" height="12"/><path d="M1 1l9 7 9-7"/></svg>
  </div>
</header>

<section class="philosophy">
  <div class="philosophy-panel"></div>
  <div class="philosophy-photo" role="img" aria-label="スーツ姿の社員が並ぶ写真"></div>
  <div class="philosophy-head"><h2>PHILOSOPHY</h2><p>企業理念</p></div>
  <p class="philosophy-statement">不動産の新しい在り方を発見し、不動産の新しい未来を創造する</p>
</section>

<section class="works">
  <div class="section-head"><h2>WORKS</h2><p>施工例</p></div>
  <div class="works-track">
    <article class="work-card left">
      <div class="work-photo" role="img" aria-label="明るい室内の施工写真" style="background:linear-gradient(135deg,#d9d9d9,#b5b5b5)"></div>
      <div class="work-caption">光が差し込む住宅</div>
    </article>
    <article class="work-card center">
      <div class="work-photo" role="img" aria-label="青空の下のモダンな二階建て住宅の写真" style="background:linear-gradient(180deg,#7fa6cf,#8a7a6a 70%,#6f6455)"></div>
      <div class="work-caption">家は楽しく生活感が暮らしやすい家</div>
      <span class="work-tag">2018.08.11 竣工</span>
    </article>
    <article class="work-card right">
      <div class="work-photo" role="img" aria-label="緑に囲まれた戸建て住宅の写真" style="background:linear-gradient(180deg,#8fb0d0,#9aa58a 65%,#6d7a5a)"></div>
      <div class="work-caption">庭でバーベキューができる家</div>
      <span class="work-tag">2018.07.12 竣工</span>
    </article>
    <span class="slider-arrow" style="left:170px;top:100px"><svg width="20" height="34" viewBox="0 0 20 34" fill="none" stroke="#fff" stroke-width="2.5"><path d="M18 2L3 17l15 15"/></svg></span>
    <span class="slider-arrow" style="left:1000px;top:100px"><svg width="20" height="34" viewBox="0 0 20 34" fill="none" stroke="#fff" stroke-width="2.5"><path d="M2 2l15 15L2 32"/></svg></span>
  </div>
  <a class="btn-outline">すべての施工例を見る <svg width="7" height="11" viewBox="0 0 7 11" fill="none" stroke="#222" stroke-width="1.5"><path d="M1 1l4.5 4.5L1 10"/></svg></a>
</section>

<section class="news">
  <div class="section-head"><h2>NEWS</h2><div class="rule"></div><p>お知らせ</p></div>
  <ul class="news-list">
    <li><time>2018.09.01</time><span>12月2日（日曜日）午後1時より完成見学会を開催します。ご家族お揃いで、お気軽にご来場ください。</span></li>
    <li><time>2018.08.24</time><span>夏季休業のお知らせ。休業期間中のお問い合わせは、休み明けより順次ご対応いたします。</span></li>
    <li><time>2018.08.03</time><span>11月4日（日曜日）午前10時より住まいの相談会を開催します。ご予約はお問い合わせフォームからどうぞ。</span></li>
    <li><time>2018.07.20</time><span>10月7日（日曜日）午後1時より完成見学会を開催します。ご来場を心よりお待ちしております。</span></li>
  </ul>
  <a class="btn-outline">一覧はこちら <svg width="7" height="11" viewBox="0 0 7 11" fill="none" stroke="#222" stroke-width="1.5"><path d="M1 1l4.5 4.5L1 10"/></svg></a>
  <div class="news-links">
    <div class="news-link dark"><div class="photo" role="img" aria-label="事業用賃貸物件の外観写真" style="background:linear-gradient(90deg,#3a3a3a,#8a8a8a)"></div><div class="label"><strong>社有事業用賃貸物件</strong><span>ご案内</span></div></div>
    <div class="news-link red"><div class="photo" role="img" aria-label="最新物件の外観写真" style="background:linear-gradient(90deg,var(--red),#7c8f6a)"></div><div class="label"><strong>最新物件情報</strong><span>オススメ物件のご紹介</span></div></div>
    <div class="news-link dark"><div class="photo" role="img" aria-label="住宅街の通りの写真" style="background:linear-gradient(90deg,#3a3a3a,#9a9a9a)"></div><div class="label"><strong>売買仲介・賃貸物件</strong><span>ご案内</span></div></div>
  </div>
</section>

<section class="company" role="img" aria-label="社屋外観の暗いトーンの写真">
  <div class="section-head"><h2>COMPANY</h2><p>会社紹介</p></div>
  <div class="company-menu"><span>ご挨拶</span><span>会社概要</span><span>会社沿革</span><span>採用情報</span></div>
</section>

<section class="access-map" role="img" aria-label="本社周辺の地図">
  <svg class="map-pin" width="40" height="54" viewBox="0 0 40 54"><path d="M20 2C10 2 2 10 2 20c0 13 18 32 18 32s18-19 18-32C38 10 30 2 20 2z" fill="var(--red)"/><circle cx="20" cy="20" r="7" fill="#fff"/></svg>
</section>

<footer class="site-footer">
  <nav class="footer-nav"><span>HOME</span><span>COMPANY</span><span>WORKS</span><span>NEWS</span><span>RECRUIT</span></nav>
  <div class="footer-contact">CONTACT <svg width="22" height="16" viewBox="0 0 22 16" fill="none" stroke="#fff" stroke-width="1.5"><rect x="1" y="1" width="20" height="14"/><path d="M1 1l10 8 10-8"/></svg></div>
  <div class="footer-tel">048-000-1234</div>
  <div class="footer-hours">営業時間 9:00〜18:00</div>
  <div class="footer-brand">
    <div class="name">AOBA ESTATE</div>
    <div class="ja">アオバエステート株式会社</div>
    <div class="addr">〒000-0000 埼玉県青葉市緑町1丁目2-3　TEL 048-000-1234　FAX 048-000-5678</div>
  </div>
  <div class="copyright">Copyright © AOBA ESTATE Co.,Ltd. All Rights Reserved.</div>
</footer>

</body>
</html>
```